Business card design to suit our website

Need a nice looking business card for our business based off images from our Website and provided images. The business card will require 2 different names (for the 2 owners). The business card should include images from our website, facebook (larkvale coil starter pack) or the pictures provided. it should also contain all contact information.
Our website is www.larkvalecoilworks.com.au
Please dont use image from top bar of website. If images are used please use the ones of our product under the buy it now tab
Updates

Need extra days to review

Target Market(s)

Automotive

Industry/Entity Type

Automotive Part

Contact Information for Business Card

Business Name. contact details including names phone number email. logo
2 business cards needed with 2 different persons names and phone number.

Colors

Designer to choose colors to be used in the design.

Requirements
Must have
• whatever looks best

```html
<!DOCTYPE html>
<html lang="en">
<head>
<meta charset="utf-8">
<title>Larkvale Coil Works – Business Card</title>
<link href="https://fonts.googleapis.com/css2?family=Roboto:wght@400;500;700&display=swap" rel="stylesheet">
<style>
  :root {
    --backdrop: #1d8ab2;
    --card-dark: #161718;
    --card-dark-mid: #2a2c2e;
    --brand-red: #c8202f;
    --paper: #ffffff;
    --ink: #333333;
    --light-text: #ffffff;
    --chrome-light: #d9dadb;
    --chrome-dark: #6d6f72;
  }
  * { box-sizing: border-box; margin: 0; padding: 0; }
  html, body { width: 1200px; height: 560px; overflow: hidden; }
  body {
    background: var(--backdrop);
    font-family: "Roboto", Arial, sans-serif;
    position: relative;
  }
  .card {
    position: absolute;
    top: 130px;
    width: 530px;
    height: 300px;
    overflow: hidden;
    box-shadow: 0 6px 18px rgba(0,0,0,0.25);
  }
  .card--front { left: 40px; background: var(--paper); }
  .card--back {
    left: 630px;
    background: radial-gradient(ellipse at 50% 50%, var(--card-dark-mid) 0%, var(--card-dark) 75%);
  }
  .card__shapes { position: absolute; inset: 0; width: 100%; height: 100%; }

  .front__vehicle-art {
    position: absolute;
    left: 300px; top: 36px;
    width: 230px; height: 150px;
    border-radius: 40% 10% 20% 45%;
    background: radial-gradient(ellipse at 60% 45%, var(--chrome-light) 0%, #a9abad 45%, var(--chrome-dark) 75%, rgba(40,42,44,0) 100%);
  }
  .front__brand {
    position: absolute;
    left: 52px; top: 26px;
    display: flex; align-items: center; gap: 6px;
    color: var(--brand-red);
    font-weight: 700;
    font-size: 13px;
    letter-spacing: 0.2px;
  }
  .brand__dot {
    width: 9px; height: 9px;
    border-radius: 50%;
    background: var(--brand-red);
  }
  .front__identity { position: absolute; left: 62px; top: 74px; color: var(--light-text); }
  .front__name { font-size: 29px; font-weight: 700; letter-spacing: 0.5px; line-height: 1; }
  .front__position { font-size: 15px; font-weight: 400; margin-top: 3px; }

  .contact-row { position: absolute; left: 0; top: 220px; width: 100%; height: 72px; }
  .contact-item {
    position: absolute;
    top: 0;
    transform: translateX(-50%);
    display: flex; flex-direction: column; align-items: center;
    font-size: 11.5px; color: var(--ink);
    text-align: center; line-height: 1.25;
    white-space: nowrap;
  }
  .contact-item--address { left: 84px; }
  .contact-item--phone { left: 235px; }
  .contact-item--email { left: 409px; }
  .contact-item__icon { width: 20px; height: 20px; margin-bottom: 12px; }

  .back__brand {
    position: absolute;
    left: 0; right: 0; top: 128px;
    display: flex; justify-content: center; align-items: center; gap: 10px;
    color: var(--brand-red);
    font-weight: 700;
    font-size: 34px;
  }
  .back__brand .brand__dot { width: 18px; height: 18px; }
</style>
</head>
<body>

  <section class="card card--front" aria-label="Business card front">
    <svg class="card__shapes" viewBox="0 0 530 300" preserveAspectRatio="none" aria-hidden="true">
      <defs>
        <linearGradient id="frontDark" x1="0" y1="0" x2="1" y2="1">
          <stop offset="0" stop-color="#1b1c1d"/>
          <stop offset="0.6" stop-color="#2b2d2f"/>
          <stop offset="1" stop-color="#1e1f20"/>
        </linearGradient>
      </defs>
      <rect x="0" y="0" width="530" height="205" fill="url(#frontDark)"/>
      <line x1="0" y1="40" x2="48" y2="40" stroke="#5a5c5f" stroke-width="1"/>
      <line x1="165" y1="40" x2="500" y2="40" stroke="#5a5c5f" stroke-width="1"/>
      <polygon points="0,180 157,180 165,203 530,203 530,300 0,300" fill="var(--paper)"/>
      <polygon points="157,190 240,190 248,203 165,203" fill="var(--brand-red)"/>
      <rect x="0" y="294" width="530" height="6" fill="var(--brand-red)"/>
    </svg>

    <div class="front__vehicle-art" role="img" aria-label="Illustration of a silver sedan, front three-quarter view"></div>

    <div class="front__brand"><span class="brand__dot"></span>Larkvale Coil Works</div>

    <div class="front__identity">
      <h1 class="front__name">YOUR NAME</h1>
      <p class="front__position">Your position</p>
    </div>

    <div class="contact-row">
      <div class="contact-item contact-item--address">
        <svg class="contact-item__icon" viewBox="0 0 20 20" aria-hidden="true">
          <circle cx="10" cy="10" r="10" fill="var(--brand-red)"/>
          <path d="M10 5 L15 9.5 H13.5 V14.5 H11 V11.5 H9 V14.5 H6.5 V9.5 H5 Z" fill="#fff"/>
        </svg>
        <span>Larkvale Coil Works<br>Address</span>
      </div>
      <div class="contact-item contact-item--phone">
        <svg class="contact-item__icon" viewBox="0 0 20 20" aria-hidden="true">
          <circle cx="10" cy="10" r="10" fill="var(--brand-red)"/>
          <path d="M7.2 5.2 L8.6 7.4 L7.6 8.4 Q8.6 10.6 11.6 12.4 L12.6 11.4 L14.8 12.8 L13.8 14.6 Q9.6 14.4 6.4 9.6 Q5.6 7.4 7.2 5.2 Z" fill="#fff"/>
        </svg>
        <span>0400 582 316</span>
      </div>
      <div class="contact-item contact-item--email">
        <svg class="contact-item__icon" viewBox="0 0 20 20" aria-hidden="true">
          <circle cx="10" cy="10" r="10" fill="var(--brand-red)"/>
          <rect x="5" y="6.5" width="10" height="7" fill="#fff"/>
          <path d="M5 6.5 L10 10.5 L15 6.5" fill="none" stroke="var(--brand-red)" stroke-width="1"/>
        </svg>
        <span>sales@larkvalecoilworks.com.au</span>
      </div>
    </div>
  </section>

  <section class="card card--back" aria-label="Business card back">
    <div class="back__brand"><span class="brand__dot"></span>Larkvale Coil Works</div>
  </section>

</body>
</html>
```